Property Management
Bryvale Management Solutions, Inc.
Professional
Nora Dellaway, CCAM
Senior Community Manager/President
4820 Marsh Hollow Lane, Suite 300
Ravenport, CA. 90412
ndellaway@bryvalemanagementsolutions.example
www.bryvalemanagementsolutions.example

```html
<!DOCTYPE html>
<html lang="en">
<head>
<meta charset="utf-8">
<title>Bryvale Management Solutions – Stationery</title>
<link href="https://fonts.googleapis.com/css2?family=Lato:wght@400;700&display=swap" rel="stylesheet">
<style>
  :root {
    --navy: #1d3f73;
    --navy-dark: #163258;
    --ink: #4a4f57;
    --paper: #ffffff;
    --stage: #e7e5e1;
    --grey-flap: #5f656c;
    --grey-light: #dfe2e5;
  }
  * { box-sizing: border-box; margin: 0; padding: 0; }
  html, body { width: 1200px; height: 466px; overflow: hidden; }
  body {
    background: var(--stage);
    font-family: "Lato", Arial, sans-serif;
    color: var(--ink);
    position: relative;
  }
  .sheet {
    position: absolute;
    background: var(--paper);
    border: 3px solid var(--navy);
    box-shadow: 0 2px 6px rgba(0,0,0,.18);
    overflow: hidden;
  }
  .brand { display: flex; flex-direction: column; gap: 2px; flex-shrink: 0; }
  .brand-mark { display: flex; align-items: center; gap: 5px; }
  .brand-square { background: var(--navy); display: block; }
  .brand-name { font-weight: 700; color: var(--navy); line-height: 1; }
  .brand-sub { color: var(--navy); font-size: 6px; line-height: 1.2; white-space: nowrap; }
  .brand-tag { color: var(--ink); font-size: 5px; line-height: 1.2; white-space: nowrap; }

  /* business cards */
  .card { width: 96px; height: 55px; left: 26px; padding: 6px; border-width: 2px; }
  .card-front { top: 175px; display: flex; align-items: center; }
  .card-front .brand-square { width: 9px; height: 9px; }
  .card-front .brand-name { font-size: 13px; }
  .card-front .brand-sub { font-size: 4.5px; }
  .card-back { top: 247px; padding: 5px 5px; }
  .card-back .person { font-size: 5.5px; font-weight: 700; color: var(--navy); white-space: nowrap; }
  .card-back .role { font-size: 4px; margin-bottom: 3px; white-space: nowrap; }
  .card-back .line { font-size: 3.4px; line-height: 1.4; white-space: nowrap; }

  /* letterheads */
  .letterhead { top: 33px; width: 283px; height: 400px; border-width: 5px; padding: 14px 14px; }
  .letterhead-one { left: 168px; }
  .letterhead-two { left: 482px; }
  .letterhead .brand-square { width: 16px; height: 16px; }
  .letterhead .brand-name { font-size: 24px; }
  .letterhead-head { display: flex; justify-content: space-between; align-items: flex-start; gap: 8px; }
  .contact-block { font-size: 4.2px; line-height: 1.6; font-style: normal; white-space: nowrap; flex-shrink: 0; margin-top: 3px; }
  .contact-block .sep { color: var(--navy); }
  .letter-footer {
    position: absolute; left: 14px; right: 14px; bottom: 10px;
    font-size: 4.2px; display: flex; gap: 10px; color: var(--ink); white-space: nowrap;
  }
  .letter-footer span::before { content: "■ "; color: var(--navy); font-size: 4px; }

  /* envelope back */
  .envelope-back { position: absolute; left: 780px; top: 33px; width: 348px; height: 267px; filter: drop-shadow(0 2px 4px rgba(0,0,0,.2)); }

  /* envelope front */
  .envelope-front { left: 780px; top: 311px; width: 348px; height: 111px; border-width: 4px; padding: 10px 12px; }
  .envelope-front .brand-square { width: 11px; height: 11px; }
  .envelope-front .brand-name { font-size: 16px; }
</style>
</head>
<body>

  <section class="sheet card card-front" aria-label="Business card front">
    <div class="brand">
      <div class="brand-mark"><span class="brand-square"></span><span class="brand-name">Bryvale</span></div>
      <span class="brand-sub">Management Solutions, Inc.</span>
    </div>
  </section>

  <section class="sheet card card-back" aria-label="Business card back">
    <p class="person">Nora Dellaway, CCAM</p>
    <p class="role">Senior Community Manager/President</p>
    <p class="line">4820 Marsh Hollow Lane, Suite 300</p>
    <p class="line">Ravenport, CA. 90412</p>
    <p class="line">ndellaway@bryvalemanagementsolutions.example</p>
    <p class="line">www.bryvalemanagementsolutions.example</p>
  </section>

  <section class="sheet letterhead letterhead-one" aria-label="Letterhead option one">
    <header class="letterhead-head">
      <div class="brand">
        <div class="brand-mark"><span class="brand-square"></span><span class="brand-name">Bryvale</span></div>
        <span class="brand-sub">Management Solutions, Inc.</span>
        <span class="brand-tag">Professional Property Management</span>
      </div>
      <address class="contact-block">
        <span class="sep">■</span> 4820 Marsh Hollow Lane, Suite 300<br>
        <span class="sep">■</span> Ravenport, CA. 90412<br>
        <span class="sep">■</span> www.bryvalemanagementsolutions.example
      </address>
    </header>
  </section>

  <section class="sheet letterhead letterhead-two" aria-label="Letterhead option two">
    <header class="letterhead-head" style="justify-content:center">
      <div class="brand">
        <div class="brand-mark"><span class="brand-square"></span><span class="brand-name">Bryvale</span></div>
        <span class="brand-sub">Management Solutions, Inc.</span>
        <span class="brand-tag">Professional Property Management</span>
      </div>
    </header>
    <footer class="letter-footer">
      <span>4820 Marsh Hollow Lane, Suite 300, Ravenport, CA. 90412</span>
      <span>www.bryvalemanagementsolutions.example</span>
    </footer>
  </section>

  <svg class="envelope-back" viewBox="0 0 348 267" aria-label="Envelope back">
    <rect x="0" y="0" width="348" height="100" fill="var(--navy)"/>
    <path d="M0 0 L348 0 L348 30 Q174 60 0 30 Z" fill="var(--navy-dark)"/>
    <rect x="0" y="100" width="348" height="78" fill="var(--grey-flap)"/>
    <rect x="0" y="178" width="348" height="89" fill="var(--paper)"/>
    <path d="M0 178 L150 230 Q174 238 198 230 L348 178 L348 267 L0 267 Z" fill="var(--grey-light)"/>
  </svg>

  <section class="sheet envelope-front" aria-label="Envelope front">
    <div class="brand">
      <div class="brand-mark"><span class="brand-square"></span><span class="brand-name">Bryvale</span></div>
      <span class="brand-sub">Management Solutions, Inc.</span>
      <span class="brand-tag">4820 Marsh Hollow Lane, Suite 300, Ravenport, CA. 90412</span>
    </div>
  </section>

</body>
</html>
```